Ridgemoor Taproom Beer Can Design

Design a beer can for a boutique craft brewery located in Frankston, Victoria, AUS.
We have a focus on producing socially approachable beers in an ambient setting. The beer can design should be sophisticated, simple, recognizable and a little playful. The color pallet should be inviting and not too bold. The design should have identifying features that can be interchanged onto different cans for different beer types. The design must be repeatable for other beer varieties, which will each have a unique color. The can should feature black, white and purple (this should be in interchangeable color). The beer can also needs to have our Ridgemoor Taproom company logo on it, this has been attached to the design brief.

Target Market(s)

The target market is aged 25+ who are social, have some disposable income and appreciate good beer, wine and food.
The beers will also be made for distribution, initially to locally to restaurants and cafés and eventually commercially.
Tourists will also be targeted due to the area the brewhouse is located (Mornington Peninsula, Victoria, AUS).

Industry/Entity Type

Hospitality

Font styles to use
Sans Serif
Script

Colors
6b449b
876aae
b7a5cd
e4daeb
000000
ffffff
959595

Requirements
Must have
• The ‘Ridgemoor Taproom’ logo.
• The colour associated to this beer - purple. This should be the only colour used on the can (along with black/white/gray).
• The company tagline ‘Socially Approachable’.
• The tasting notes text ‘Bright in colour, dry on the palate and thirst quenching in the extreme, wheat and pale malts compliment each other with nuance.’
• Australian beer can requirements as per 'Requirements.png'. EPS and AI files of the requirements have been included.
Nice to have
• The logo text ‘Cecil Grain IPA’ more predominant than the Ridgemoor Taproom logo.
Should not have
• Be busy, simple is best
• Beer related pictures / images
• Bold, masculine lines and fonts
• Requirements.png directly used. Please use the EPS or AI files provided.

```html
<!DOCTYPE html>
<html lang="en">
<head>
<meta charset="utf-8">
<title>Ridgemoor Taproom – Cecil Grain IPA Can Label</title>
<link href="https://fonts.googleapis.com/css2?family=Federo&family=Josefin+Sans:wght@300;400;600&display=swap" rel="stylesheet">
<style>
  :root {
    --backdrop: #e4daeb;
    --label-white: #ffffff;
    --ink: #000000;
    --ink-soft: #1a1a1a;
    --beer-purple: #6b449b;
    --purple-deep: #5a3689;
    --gold: #c9a24a;
    --grey: #959595;
  }
  * { margin: 0; padding: 0; box-sizing: border-box; }
  html, body { width: 967px; height: 1200px; overflow: hidden; }
  body {
    background: var(--backdrop);
    position: relative;
    font-family: "Josefin Sans", sans-serif;
  }
  .can-label {
    position: absolute;
    left: 186px; top: 130px;
    width: 594px; height: 936px;
    background: var(--label-white);
    overflow: hidden;
  }
  .colour-band {
    position: absolute;
    left: 0; right: 0; top: 648px; bottom: 0;
    background: linear-gradient(180deg, var(--beer-purple), var(--purple-deep));
  }
  .gold-rule {
    position: absolute;
    left: 0; right: 0; top: 640px;
    height: 3px;
    background: var(--gold);
  }
  .frame {
    position: absolute;
    border: 1.5px solid var(--ink-soft);
  }
  .frame--outer { left: 52px; top: 160px; width: 488px; height: 696px; }
  .frame--inner { left: 62px; top: 170px; width: 468px; height: 676px; }
  .beer-name {
    position: absolute;
    left: 62px; width: 468px; top: 272px;
    text-align: center;
    font-family: "Federo", sans-serif;
    font-weight: 400;
    color: var(--ink);
    line-height: 1;
  }
  .beer-name__line {
    display: block;
    font-size: 82px;
    letter-spacing: 4px;
  }
  .beer-name__line + .beer-name__line { margin-top: 6px; }
  .beer-name__word { position: relative; }
  .beer-name__style {
    position: absolute;
    left: 100%;
    bottom: 26px;
    margin-left: 8px;
    font-size: 30px;
    letter-spacing: 3px;
    white-space: nowrap;
  }
  .tagline {
    position: absolute;
    left: 0; right: 0; top: 518px;
    text-align: center;
    font-size: 26px;
    font-weight: 400;
    color: var(--ink);
    letter-spacing: 0.5px;
  }
  .tagline-rule {
    position: absolute;
    left: 147px; top: 556px;
    width: 300px; height: 14px;
  }
  .volume {
    position: absolute;
    left: 0; right: 0; top: 598px;
    text-align: center;
    font-size: 22px;
    font-weight: 600;
    color: var(--ink);
  }
  .brand {
    position: absolute;
    left: 62px; width: 468px; top: 730px;
    text-align: center;
    color: var(--label-white);
    font-weight: 300;
    font-size: 34px;
    letter-spacing: 6px;
    line-height: 1.3;
    text-transform: uppercase;
  }
</style>
</head>
<body>
  <main class="can-label">
    <div class="colour-band"></div>
    <div class="gold-rule"></div>
    <div class="frame frame--outer"></div>
    <div class="frame frame--inner"></div>

    <h1 class="beer-name">
      <span class="beer-name__line">CECIL</span>
      <span class="beer-name__line"><span class="beer-name__word">GRAIN<span class="beer-name__style">IPA</span></span></span>
    </h1>

    <p class="tagline">Socially Approachable</p>
    <svg class="tagline-rule" viewBox="0 0 300 14" aria-hidden="true">
      <line x1="0" y1="4" x2="300" y2="4" stroke="#000" stroke-width="1.5"/>
      <polygon points="150,0 155,7 150,14 145,7" fill="#000"/>
    </svg>

    <p class="volume">375ML</p>

    <p class="brand">Ridgemoor<br>Taproom</p>
  </main>
</body>
</html>
```